Web design for software company

I'm a software developer that designs high end specialist web applications, mobile apps and user friendly applications for medium to large customers. I integrate different systems together within a company and provide web based applications or mobile apps to view and edit information in that web of linked systems.

I currently work alone, basically selling my time on specialist projects, but also build my own software solutions which I eventually want to put into the market.

My company name is Overthread (lowercase 'L' for logic) and I work from the Netherlands. I've attached my current logo which is basically just text in VOXbox font. Current colours are mustard yellow and grey, but i'm open to other options to better fit the web design.

I've got a sort of slogan: "Specialized software development" - better ideas are welcome. The slogan in the logo attachment is older.

I'm looking for a site design that reflects my work as being on the cutting edge of technology, but being clear and simple. My thinking with the name Overthread is that it refers to the underlying mechanism and logic of software.

The site will not be text heavy, so some kind of large graphic to do with software design is welcome. I expect about 4 or 5 main pages or sections of the site in which i'll eventually add things like a blog or contact info etc.

Industry/Entity Type

It Company

Number of Pages Required

1 page

Font styles to use
Sans Serif

Requirements
Nice to have
• A large graphic or photo relevant to my focus as a software developer. Something that shows connecting of software systems with perhaps a variety of devices/browsers that would display data from that cloud of systems.
• Something like these (allthough these are ugly - but the idea is what i mean):
• http://img4.pixvaultimages.example/2000517/22458/i/450/pixvault_224581133-Cloud-computing-user-interface.jpg
• http://business.tamblinet.example/images/modules/mobile-device-policy-design-banner.png
• https://www.pagecraftly.example/images/responsive-web-design.jpg
• http://www.norvexa.example/images/web_apps.png
• https://www.keyportal.example/assets/img/product/web-app@2x.png?v2
Should not have
• Photographs of smiling happy people looking at a screen that make it look like it's a huge business with many offices. I'm a one-man company which could perhaps grow a little bit, but i want to focus on my expertise instead of size.

```html
<!DOCTYPE html>
<html lang="en">
<head>
<meta charset="utf-8">
<title>Overthread — Custom Software Solutions</title>
<link rel="stylesheet" href="https://fonts.googleapis.com/css2?family=Open+Sans:wght@400;600;700;800&family=Oswald:wght@500;600&display=swap">
<style>
:root{
  --yellow:#fcd526;
  --dark:#2e3136;
  --footer:#303338;
  --ink:#222428;
  --body:#5b5e63;
  --muted:#9a9da2;
  --line:#e4e4e4;
  --white:#ffffff;
}
*{box-sizing:border-box;margin:0;padding:0}
html,body{width:1200px;height:3197px;overflow:hidden;background:var(--white)}
body{font-family:"Open Sans",Arial,sans-serif;color:var(--body);position:relative}
.abs{position:absolute}
p{font-size:13px;line-height:23px}

/* hero */
.hero{position:absolute;left:0;top:0;width:1200px;height:690px}
.hero svg.bg{position:absolute;left:0;top:0}
.brand{position:absolute;left:70px;top:22px;display:flex;align-items:center;gap:10px}
.brand-mark{width:14px;height:40px;background:var(--yellow)}
.brand-name{font-weight:800;font-size:38px;letter-spacing:1px;color:var(--white);line-height:40px}
.brand-tag{position:absolute;left:94px;top:66px;font-size:11px;letter-spacing:1px;color:var(--yellow);font-weight:600}
.nav{position:absolute;top:36px;left:650px;display:flex;gap:36px;font-size:13px;font-weight:700;color:var(--ink)}
.nav .active{border-bottom:2px solid var(--ink);padding-bottom:4px}
.headline{position:absolute;left:612px;top:198px;font-family:"Oswald","Arial Narrow",sans-serif;font-weight:600;color:var(--ink);line-height:.9;text-transform:uppercase}
.headline span{display:block}
.hl-big{font-size:72px}
.hl-mid{font-size:38px}
.art-monitor{position:absolute;left:130px;top:80px;width:520px;height:470px;border-radius:10px;background:linear-gradient(135deg,#dfe6ec,#9fb3c4 55%,#f3e6c0)}
.art-phone{position:absolute;left:815px;top:128px;width:340px;height:490px;border-radius:30px;background:linear-gradient(160deg,#3a3d42,#1f2124 40%,#c9a64a 70%,#7bc043)}

/* about */
.about-art{position:absolute;left:75px;top:756px;width:362px;height:363px;border-radius:50%;background:radial-gradient(circle at 60% 55%,#3d4046 0 30%,#eceff1 31%)}
.section-title{font-size:20px;font-weight:600;color:var(--ink)}
.rule{position:absolute;width:96px;height:4px;background:var(--yellow)}

/* services */
.service{position:absolute;top:1187px;width:240px}
.service .icon{width:110px;height:110px;border-radius:50%;border:2px solid #ececec;display:flex;align-items:center;justify-content:center;margin-bottom:22px}
.service .icon.on{background:var(--yellow);border-color:var(--yellow)}
.service h3{font-size:15px;font-weight:600;color:var(--ink);line-height:21px;margin-bottom:16px}
.service p{font-size:12.5px;line-height:21px}

/* testimonial + blog */
.quote-title{font-size:22px;font-weight:700;color:var(--ink);text-align:center;line-height:28px}
.avatar{position:absolute;left:203px;top:1912px;width:80px;height:80px;border-radius:50%;background:#dfe3e6;border:4px solid var(--white)}
.dots{position:absolute;left:205px;top:2082px;display:flex;gap:6px}
.dots i{width:11px;height:11px;border-radius:50%;background:#c9a91a}
.dots i.on{background:var(--ink)}
.blog-title{font-size:14.5px;font-weight:700;color:var(--white);line-height:21px}
.blog-meta{font-size:11px;font-weight:600;color:var(--yellow);margin:4px 0 12px}
.blog p{color:#b7babf;font-size:12.5px;line-height:22px}

/* portfolio */
.btn-outline{position:absolute;left:737px;top:2563px;width:169px;height:46px;border:2px solid var(--yellow);display:flex;align-items:center;justify-content:center;font-size:13px;font-weight:600;color:var(--ink)}

/* clients */
.clients{position:absolute;left:0;top:2717px;width:1200px;height:106px;display:flex;border-top:1px solid var(--line)}
.clients div{flex:1;display:flex;align-items:center;justify-content:center;gap:10px;border-right:1px solid var(--line);color:#b9bbbe;font-size:15px;font-weight:600;letter-spacing:1px}
.clients div:last-child{border-right:none}
.clients b{width:30px;height:30px;border-radius:50%;background:#d8d9db;display:block}

/* footer */
.newsletter{position:absolute;left:0;top:2823px;width:1200px;height:90px;background:var(--footer);border-bottom:1px solid #43464b}
.signup{position:absolute;left:882px;top:2849px;width:115px;height:38px;border-radius:19px;background:var(--yellow);display:flex;align-items:center;justify-content:space-between;padding:0 6px 0 18px;font-size:13px;font-weight:700;color:var(--ink)}
.signup i{width:26px;height:26px;border-radius:50%;background:var(--ink);display:flex;align-items:center;justify-content:center}
.footer{position:absolute;left:0;top:2913px;width:1200px;height:284px;background:var(--footer)}
.foot-h{font-size:14px;font-weight:700;color:var(--white);margin-bottom:10px}
.foot-list{font-size:12.5px;line-height:22px;color:#c9cbce;list-style:none}
.map{position:absolute;left:75px;top:2958px;width:149px;height:111px;background:linear-gradient(135deg,#e9e6df,#cfd6cc)}
.socials{position:absolute;left:75px;top:3139px;display:flex;gap:6px}
.socials i{width:30px;height:30px;border-radius:50%;border:2px solid #c9cbce;display:block}
</style>
</head>
<body>

<header class="hero">
  <svg class="bg" width="1200" height="690" viewBox="0 0 1200 690" aria-hidden="true">
    <polygon points="0,0 600,0 600,686 0,686" fill="#2e3136"/>
    <polygon points="600,0 1200,0 1200,650 600,686" fill="#fcd526"/>
  </svg>
  <div class="art-monitor" role="img" aria-label="Desktop monitor with stacked website layouts fanning out"></div>
  <div class="art-phone" role="img" aria-label="Smartphone shaped like a shop stall with shelves and a shopping basket"></div>
  <div class="brand"><span class="brand-mark"></span><span class="brand-name">OVERTHREAD</span></div>
  <div class="brand-tag">CUSTOM SOFTWARE SOLUTIONS</div>
  <nav class="nav">
    <span class="active">HOME</span><span>ABOUT</span><span>SERVICES</span><span>PORTFOLIO</span><span>BLOG</span><span>CONTACT</span>
  </nav>
  <h1 class="headline">
    <span class="hl-big">High</span>
    <span class="hl-mid">End</span>
    <span class="hl-big">Web</span>
    <span class="hl-mid">And</span>
    <span class="hl-big">Mobile</span>
    <span class="hl-mid" style="font-size:42px">Applications</span>
  </h1>
</header>

<section class="about">
  <div class="about-art" role="img" aria-label="Flat illustration of a tablet, code window, gear and ruler for software design"></div>
  <h2 class="section-title abs" style="left:567px;top:818px">Software Development Company</h2>
  <div class="rule" style="left:567px;top:864px"></div>
  <p class="abs" style="left:567px;top:900px;width:560px">Lorem Ipsum is simply dummy text of the printing and type setting into industry. Lorem Ipsum has been the industry's standard dummy text ever since the 1500s, when an unknown printer took a galley of type scrambled it to make a type specimen book. It has survived not only five centuries, but also the leap into electronic typesetting, remaining Letraset sheets containing Lorem Ipsum passages, and more recently with desktop publishing software like Aldus PageMaker including versions of Lorem Ipsum.</p>
</section>

<section class="services">
  <div class="service" style="left:75px">
    <div class="icon"><svg width="44" height="40" viewBox="0 0 44 40" fill="none" stroke="#9a9da2" stroke-width="2"><rect x="2" y="2" width="40" height="30" rx="2"/><line x1="2" y1="9" x2="42" y2="9"/><rect x="8" y="14" width="12" height="12"/><line x1="24" y1="15" x2="36" y2="15"/><line x1="24" y1="21" x2="36" y2="21"/></svg></div>
    <h3>Web Application<br>Development</h3>
    <p>Lorem Ipsum is simply dummy text of the into has been the industry's the 1500s.</p>
  </div>
  <div class="service" style="left:345px">
    <div class="icon on"><svg width="44" height="44" viewBox="0 0 44 44" fill="none" stroke="#222428" stroke-width="2.2"><path d="M12 38v-8c-4-3-6-7-6-12a16 16 0 0 1 32 0l3 6h-4v6a3 3 0 0 1-3 3h-4v5"/><circle cx="22" cy="18" r="5"/></svg></div>
    <h3>Custom Software<br>Development</h3>
    <p>Lorem Ipsum is simply dummy text of the into has been the industry's the 1500s.</p>
  </div>
  <div class="service" style="left:614px">
    <div class="icon"><svg width="44" height="44" viewBox="0 0 44 44" fill="none" stroke="#9a9da2" stroke-width="2"><rect x="6" y="4" width="16" height="28" rx="2"/><rect x="22" y="12" width="16" height="28" rx="2"/><line x1="10" y1="10" x2="18" y2="10"/><line x1="26" y1="18" x2="34" y2="18"/></svg></div>
    <h3>Enterprise Mobile<br>Applications</h3>
    <p>Lorem Ipsum is simply dummy text of the into has been the industry's the 1500s.</p>
  </div>
  <div class="service" style="left:884px">
    <div class="icon"><svg width="44" height="44" viewBox="0 0 44 44" fill="none" stroke="#9a9da2" stroke-width="2"><rect x="8" y="4" width="28" height="34" rx="2"/><line x1="14" y1="12" x2="30" y2="12"/><line x1="14" y1="18" x2="30" y2="18"/><line x1="14" y1="24" x2="24" y2="24"/><path d="M4 30h10v10H4z"/></svg></div>
    <h3>Online Collaboration<br>Platforms</h3>
    <p>Lorem Ipsum is simply dummy text of the into has been the industry's the 1500s.</p>
  </div>
</section>

<section class="feedback">
  <svg class="abs" style="left:0;top:1480px" width="1200" height="685" viewBox="0 0 1200 685" aria-hidden="true">
    <rect x="0" y="27" width="440" height="650" fill="#fcd526"/>
    <polygon points="435,37 1200,5 1200,630 435,662" fill="#2e3136"/>
  </svg>
  <h2 class="quote-title abs" style="left:40px;top:1574px;width:440px">What The Clients Talking<br>About Us</h2>
  <svg class="abs" style="left:222px;top:1668px" width="42" height="32" viewBox="0 0 42 32" fill="none" stroke="#222428" stroke-width="2.5"><path d="M16 4C8 6 4 12 4 20a6 6 0 1 0 6-6"/><path d="M36 4c-8 2-12 8-12 16a6 6 0 1 0 6-6"/></svg>
  <p class="abs" style="left:70px;top:1724px;width:345px;text-align:center;color:#4a4430;font-size:12.5px">Lorem Ipsum is simply dummy text of the printing and type setting into industry. Lorem Ipsum has been the industry's standard dummy text ever since the 1500s, when an unknown printer took a galley of type scrambled it to make a type specimen book.</p>
  <div class="avatar" role="img" aria-label="Client portrait"></div>
  <div class="abs" style="left:40px;top:2013px;width:405px;text-align:center;font-size:15px;font-weight:700;color:var(--ink)">Mara Levens</div>
  <div class="abs" style="left:40px;top:2039px;width:405px;text-align:center;font-size:13px;color:#4a4430">Lorem Ipsum is simply</div>
  <div class="dots"><i class="on"></i><i></i><i></i><i></i><i></i></div>

  <h2 class="abs" style="left:524px;top:1574px;font-size:22px;font-weight:600;color:var(--white)">Latest Blog Posts</h2>
  <div class="abs" style="left:524px;top:1658px;width:179px;height:124px;background:linear-gradient(135deg,#5c6f82,#c9d3db 60%,#8a5a4a)" role="img" aria-label="Hand holding a tablet showing analytics charts"></div>
  <div class="blog abs" style="left:731px;top:1652px;width:400px">
    <div class="blog-title">The standard Lorem Ipsum pas used since 2016</div>
    <div class="blog-meta">20 Jun 2016 &nbsp;|&nbsp; 02 Comments</div>
    <p>Lorem Ipsum is simply dummy text of the printing and type setting into industry. Lorem Ipsum has been the industry's unknown printer took a galley of type scrambled it to make a type specimen book.</p>
  </div>
  <div class="abs" style="left:524px;top:1854px;width:600px;height:1px;background:#474a50"></div>
  <div class="abs" style="left:825px;top:1885px;width:1px;height:175px;background:#474a50"></div>
  <div class="blog abs" style="left:524px;top:1888px;width:270px">
    <div class="blog-title">The standard Lorem Ipsum pas used since 2016</div>
    <div class="blog-meta">20 Jun 2016 &nbsp;|&nbsp; 02 Comments</div>
    <p>Lorem Ipsum is simply dummy text of the printing and type setting into galley of type scrambled it to make a type specimen book.</p>
  </div>
  <div class="blog abs" style="left:884px;top:1888px;width:270px">
    <div class="blog-title">The standard Lorem Ipsum pas used since 2016</div>
    <div class="blog-meta">20 Jun 2016 &nbsp;|&nbsp; 02 Comments</div>
    <p>Lorem Ipsum is simply dummy text of the printing and type setting into galley of type scrambled it to make a type specimen book.</p>
  </div>
</section>

<section class="portfolio">
  <h2 class="section-title abs" style="left:70px;top:2246px">Portfolio of work</h2>
  <div class="rule" style="left:70px;top:2292px"></div>
  <div class="abs" style="left:75px;top:2323px;width:607px;height:330px;background:linear-gradient(135deg,#f1f1f1,#d9d9d9 50%,#e9c84a 75%,#3a3d42)" role="img" aria-label="Website mockup shown on tablet, desktop and phone screens"></div>
  <h3 class="abs" style="left:737px;top:2335px;font-size:15px;font-weight:600;color:var(--ink)">Halden Design Studio</h3>
  <p class="abs" style="left:737px;top:2370px;width:400px;font-size:12.5px">Lorem Ipsum is simply dummy text of the printing and type setting into industry. Lorem Ipsum has been the industry's standard dummy text ever since the 1500s, when an info unknown printer took a galley of type scrambled it to make a type specimen book. It has survived not only five lipsum passages, and more recently with desktop publishing Aldus PageMaker including versions of Lorem Ipsum.</p>
  <div class="btn-outline">VIEW PORTFOLIO</div>
</section>

<section class="clients">
  <div><b></b>BRIGHTMOOR</div>
  <div><b></b>BRIGHTMOOR</div>
  <div><b></b>BRIGHTMOOR</div>
  <div><b></b>BRIGHTMOOR</div>
</section>

<section class="newsletter">
  <div class="abs" style="left:198px;top:32px;font-size:17px;font-weight:700;color:var(--white)">Let's Stay Connected!</div>
  <div class="abs" style="left:465px;top:26px;width:400px;font-size:12.5px;line-height:19px;color:#c9cbce">Sign up today for our newsletter and receive latest news and also get our tips &amp; exclusive offers.</div>
</section>
<div class="signup">SIGN UP <i><svg width="10" height="10" viewBox="0 0 10 10"><path d="M3 1l4 4-4 4" fill="none" stroke="#fcd526" stroke-width="2"/></svg></i></div>

<footer class="footer">
  <div class="abs" style="left:251px;top:50px;width:240px">
    <div class="foot-h">OVERTHREAD</div>
    <ul class="foot-list">
      <li>228, Lorem ipsum dolor sit,</li>
      <li>dosos amet dill - 845848</li>
      <li style="margin-top:10px">T: 1800 555 0142</li>
      <li>E: info@overthread.example</li>
      <li>www.overthread.example</li>
    </ul>
  </div>
  <div class="abs" style="left:550px;top:50px">
    <div class="foot-h">OUR SERVICES</div>
    <ul class="foot-list">
      <li>Web Application Development</li>
      <li>Custom Software Development</li>
      <li>Enterprise Mobile Applications</li>
      <li>Online Collaboration Platforms</li>
    </ul>
  </div>
  <div class="abs" style="left:882px;top:50px">
    <div class="foot-h">QUICK LINKS</div>
    <ul class="foot-list">
      <li>Home</li><li>About</li><li>Services</li><li>Portfolio</li><li>Blog</li><li>Contact</li>
    </ul>
  </div>
  <div class="abs" style="left:256px;top:232px;font-size:12px;color:#c9cbce">© 2016 Overthread. All Rights Reserved</div>
</footer>
<div class="map" role="img" aria-label="Street map showing the office location"></div>
<svg class="abs" style="left:135px;top:2985px" width="26" height="36" viewBox="0 0 26 36" aria-hidden="true"><path d="M13 35C13 35 2 20 2 13a11 11 0 0 1 22 0c0 7-11 22-11 22z" fill="#e23b3b"/><circle cx="13" cy="13" r="4" fill="#fff"/></svg>
<div class="socials"><i></i><i></i><i></i><i></i><i></i></div>

</body>
</html>
```